Communication Business Card Design

We offer complete cabling solutions
Data Cabling,Fibre Optic, and Cabling Repairs fault finding
Security camera installation
TV Aerial installation
Security alarm installation
HWR

Industry/Entity Type

Business

Contact Information for Business Card

Brightmoor Solutions
ABN 58 214 992 367
EMAIL brightmoorsolutions.com.au
Mobile 0491236057
Lou Archer

```html
<!DOCTYPE html>
<html lang="en">
<head>
<meta charset="utf-8">
<title>Brightmoor Solutions – Business Card</title>
<link rel="stylesheet" href="https://fonts.googleapis.com/css2?family=Montserrat:wght@700&family=Roboto+Condensed:wght@400;700&family=Quicksand:wght@400&display=swap">
<style>
  :root {
    --page: #ffffff;
    --ink: #000000;
    --paper: #ffffff;
    --accent-yellow: #f2e600;
    --cable-blue: #2a3fb0;
    --cable-yellow: #e0c21a;
    --cable-green: #3a9a3a;
    --cable-dark: #1a1c14;
    --fibre-orange: #f0602a;
    --back-light: #eeeeee;
  }
  html, body {
    margin: 0;
    width: 1200px;
    height: 1000px;
    overflow: hidden;
    background: var(--page);
  }
  .canvas {
    position: relative;
    width: 1200px;
    height: 1000px;
  }
  .card {
    position: absolute;
    left: 199px;
    width: 798px;
    overflow: hidden;
  }
  .card--front {
    top: 94px;
    height: 380px;
  }
  .card--back {
    top: 499px;
    height: 403px;
    width: 796px;
  }
  .photo {
    position: absolute;
    inset: 0;
  }
  .photo--cables {
    background:
      radial-gradient(ellipse 260px 150px at 540px 300px, rgba(224,194,26,0.95), rgba(58,154,58,0.6) 60%, transparent 100%),
      linear-gradient(90deg, var(--cable-blue) 0%, #22308a 30%, #2b2e22 55%, var(--cable-dark) 100%);
  }
  .photo--fibre {
    background:
      radial-gradient(ellipse 360px 160px at 640px 120px, rgba(240,96,42,0.85), rgba(240,96,42,0.25) 70%, transparent 100%),
      linear-gradient(180deg, #f4f4f4 0%, var(--back-light) 100%);
  }
  .brand-pill {
    position: absolute;
    left: 84px;
    top: 253px;
    width: 617px;
    height: 54px;
    border-radius: 27px;
    background: var(--ink);
    color: var(--paper);
    font-family: "Montserrat", sans-serif;
    font-weight: 700;
    font-size: 37px;
    letter-spacing: 0.5px;
    line-height: 54px;
    text-align: center;
  }
  .services {
    position: absolute;
    left: 0;
    right: 0;
    top: 18px;
    text-align: center;
    color: var(--ink);
    font-family: "Roboto Condensed", sans-serif;
  }
  .services__title {
    margin: 0;
    font-weight: 700;
    font-size: 37px;
    line-height: 46px;
  }
  .services__list {
    margin: 0;
    padding: 0;
    list-style: none;
    font-size: 25px;
    line-height: 37.5px;
  }
  .contact-bar {
    position: absolute;
    left: 11px;
    right: 13px;
    top: 317px;
    height: 70px;
    background: var(--ink);
    color: var(--paper);
    font-family: "Quicksand", sans-serif;
    font-weight: 400;
  }
  .contact-bar__person {
    position: absolute;
    left: 12px;
    top: 4px;
  }
  .contact-bar__business {
    position: absolute;
    right: 12px;
    top: 4px;
    text-align: right;
  }
  .contact-bar p { margin: 0; }
  .contact-bar__name {
    color: var(--accent-yellow);
    font-size: 28px;
    line-height: 32px;
  }
  .contact-bar__mobile {
    font-size: 30px;
    line-height: 34px;
  }
  .contact-bar__abn {
    font-size: 27px;
    line-height: 32px;
  }
  .contact-bar__email {
    font-size: 22px;
    line-height: 34px;
  }
</style>
</head>
<body>
<main class="canvas">
  <section class="card card--front">
    <div class="photo photo--cables" role="img" aria-label="Close-up photo of coiled blue data cables, green and yellow earth cables and dark wiring"></div>
    <div class="brand-pill">Brightmoor Solutions</div>
  </section>

  <section class="card card--back">
    <div class="photo photo--fibre" role="img" aria-label="Photo of orange fibre optic patch leads with two metal connectors on a white surface"></div>
    <div class="services">
      <h2 class="services__title">We offer complete cabling solutions in...</h2>
      <ul class="services__list">
        <li>Data Cabling, Fibre Optic, and Cabling Repairs fault finding.</li>
        <li>Security alarm installation.&nbsp; Security camera installation.</li>
        <li>TV Aerial installation.</li>
        <li>HWR.</li>
      </ul>
    </div>
    <div class="contact-bar">
      <div class="contact-bar__person">
        <p class="contact-bar__name">Lou Archer</p>
        <p class="contact-bar__mobile">Mobile 0491236057</p>
      </div>
      <div class="contact-bar__business">
        <p class="contact-bar__abn">ABN 58 214 992 367</p>
        <p class="contact-bar__email">EMAIL brightmoorsolutions.com.au</p>
      </div>
    </div>
  </section>
</main>
</body>
</html>
```